vortane realty business card

We need a Business card for our new business. The logo was designed by ArtQuillo, and the text We want on the back is:
REAL ESTATE INVESTMENTS
- BUY, RENOVATE, SELL AND RENT RESIDENTIAL PROPERTIES
- FULL HOME REHABBING , REMODELING AND INTERIOR DESIGN
- HOME STAGING SERVICES
- WHOLESALE INVESTOR PROPERTIES
- MAKE CASH OFFERS ON HOUSES IN ANY CONDITION AND IN ANY SITUATION
- PRIVATE MONEY INVESTOR PROGRAMS WITH 6-12% RETURNS
- PAY CASH REWARDS FOR REFFERALS
- CONCIERGE SERVICE

```html
<!DOCTYPE html>
<html lang="en">
<head>
<meta charset="utf-8">
<title>Vortane Realty – Business Card</title>
<link href="https://fonts.googleapis.com/css2?family=Exo+2:wght@400;600;700&display=swap" rel="stylesheet">
<style>
  :root {
    --canvas-bg: #eceae6;
    --teal: #6fc5cc;
    --teal-deep: #4fb4c4;
    --grey: #7d7f82;
    --grey-dark: #6c6e70;
    --white: #ffffff;
  }
  * { box-sizing: border-box; margin: 0; padding: 0; }
  html, body {
    width: 1200px; height: 1000px; overflow: hidden;
    background: var(--canvas-bg);
    font-family: "Exo 2", sans-serif;
  }
  .sheet {
    position: relative; width: 1200px; height: 1000px;
  }
  .card {
    position: absolute; left: 200px; width: 800px; height: 457px;
    box-shadow: 0 6px 22px rgba(0,0,0,0.12);
    overflow: hidden;
  }
  /* Back side */
  .card--back { top: 30px; background: var(--teal); color: var(--white); }
  .services { position: absolute; left: 56px; top: 52px; width: 600px; }
  .services__title {
    font-weight: 700; font-size: 24px; letter-spacing: 1px; margin-bottom: 12px;
  }
  .services__list { list-style: none; }
  .services__item {
    font-size: 16px; letter-spacing: 0.6px; line-height: 1.45;
    padding-left: 16px; position: relative; text-transform: uppercase;
  }
  .services__item::before { content: "-"; position: absolute; left: 0; }
  .back-brand {
    position: absolute; right: 48px; bottom: 40px; text-align: right;
  }
  .back-brand__name { font-size: 22px; font-weight: 600; }
  .back-brand__tag { font-size: 10px; letter-spacing: 1.5px; margin-top: 2px; }

  /* Front side */
  .card--front { top: 513px; background: var(--white); }
  .brand { position: absolute; left: 60px; top: 62px; }
  .brand__row { display: flex; align-items: center; gap: 16px; }
  .brand__mark { width: 26px; height: 26px; background: var(--teal); }
  .brand__name {
    font-size: 52px; font-weight: 600; color: var(--teal-deep); letter-spacing: 1px; line-height: 1;
  }
  .brand__tag {
    font-size: 25px; color: var(--grey); letter-spacing: 2px; margin-top: 8px; margin-left: 42px;
  }
  .contact { position: absolute; left: 66px; top: 270px; list-style: none; }
  .contact__item {
    display: flex; align-items: center; gap: 14px;
    font-size: 20px; color: var(--grey); line-height: 1; margin-bottom: 15px;
  }
  .contact__icon { width: 22px; height: 22px; flex: none; }
  .person { position: absolute; right: 62px; top: 280px; text-align: right; }
  .person__name { font-size: 30px; color: var(--teal); }
  .person__title { font-size: 22px; color: var(--grey-dark); margin-top: 10px; }
</style>
</head>
<body>
<main class="sheet">

  <section class="card card--back" aria-label="Card back">
    <div class="services">
      <h2 class="services__title">REAL ESTATE INVESTMENTS</h2>
      <ul class="services__list">
        <li class="services__item">Buy, renovate, sell and rent residential properties</li>
        <li class="services__item">Full home rehabbing, remodeling and interior design</li>
        <li class="services__item">Home staging services</li>
        <li class="services__item">Wholesale investor properties</li>
        <li class="services__item">Make cash offers on houses in any condition and in any situation</li>
        <li class="services__item">Private money investor programs with 6-12% returns</li>
        <li class="services__item">Pay cash rewards for refferals</li>
        <li class="services__item">Concierge service</li>
      </ul>
    </div>
    <div class="back-brand">
      <div class="back-brand__name">Vortane Realty</div>
      <div class="back-brand__tag">REAL ESTATE SOLUTIONS</div>
    </div>
  </section>

  <section class="card card--front" aria-label="Card front">
    <div class="brand">
      <div class="brand__row">
        <span class="brand__mark"></span>
        <span class="brand__name">Vortane Realty</span>
      </div>
      <div class="brand__tag">REAL ESTATE SOLUTIONS</div>
    </div>

    <ul class="contact">
      <li class="contact__item">
        <svg class="contact__icon" viewBox="0 0 24 24"><path d="M12 2a7 7 0 0 0-7 7c0 5 7 13 7 13s7-8 7-13a7 7 0 0 0-7-7zm0 9.5A2.5 2.5 0 1 1 12 6.5a2.5 2.5 0 0 1 0 5z" fill="var(--teal)"/></svg>
        <span>Address: To be confirmed</span>
      </li>
      <li class="contact__item">
        <svg class="contact__icon" viewBox="0 0 24 24"><rect x="6" y="2" width="12" height="20" rx="2" fill="none" stroke="var(--teal)" stroke-width="2"/><circle cx="12" cy="18" r="1.2" fill="var(--teal)"/></svg>
        <span>Phone: To be confirmed</span>
      </li>
      <li class="contact__item">
        <svg class="contact__icon" viewBox="0 0 24 24"><rect x="7" y="2" width="10" height="7" fill="var(--teal)"/><rect x="2" y="9" width="20" height="13" rx="2" fill="var(--teal)"/><rect x="6" y="13" width="12" height="2" fill="#fff"/><rect x="6" y="17" width="12" height="2" fill="#fff"/></svg>
        <span>Fax: To be confirmed</span>
      </li>
      <li class="contact__item">
        <svg class="contact__icon" viewBox="0 0 24 24"><rect x="2" y="5" width="20" height="14" rx="1" fill="var(--teal)"/><path d="M2 6l10 7 10-7" fill="none" stroke="#fff" stroke-width="1.5"/></svg>
        <span>Email: mara@kelvinmoor.com.au</span>
      </li>
    </ul>

    <div class="person">
      <div class="person__name">Your Name here</div>
      <div class="person__title">Title here</div>
    </div>
  </section>

</main>
</body>
</html>
```